Website for Fashion/Jewelry online seller

We would like a website design that can be used in wordpress. It will be important to be able to link instagram, twitter, etc posts on the bottom of site. We are to be a online seller of chic jewelry, art, fashion, and other home design industries. Currently we emphasize jewelry but as the years move forward, other products will be introduced as collections in home furnishings and primarily women's fashion. It will be important to have a “shop now” section where people can order products online so ecommerce will need to be set up at some point. The website should have the following feel: clean, modern, contemporary and chic. A lot of whites should be used with simple text and simple but elegant fonts. Best is to go to mirevantello.com to get the best idea of what we are wanting for the look and feel of the site.

Target Market(s)

upper social class people that are into fashion, jewelry, etc

Industry/Entity Type

Fashion

Number of Pages Required

5+ page

Font styles to use
Other font styles liked:
• go to daskorvin.com to see the font desired

Requirements
Must have
• Name of Company is Tide Hollow 7
Nice to have
• see project description
Should not have
• see project description

```html
<!DOCTYPE html>
<html lang="en">
<head>
<meta charset="utf-8">
<title>Tide Hollow 7</title>
<link rel="stylesheet" href="https://fonts.googleapis.com/css2?family=Exo+2:wght@400;500;600;700&family=Great+Vibes&family=Open+Sans:wght@400;600&display=swap">
<style>
:root{
  --gold:#f6b72c;
  --ink:#1f1f1f;
  --muted:#666;
  --panel:#f4f4f4;
  --foot:#2e2e2e;
  --foot-mid:#242424;
  --white:#fff;
}
*{box-sizing:border-box;margin:0;padding:0}
html,body{width:735px;height:1200px;overflow:hidden;background:var(--white)}
body{position:relative;font-family:"Open Sans",sans-serif;color:var(--ink)}
.abs{position:absolute}

/* hero */
.hero{left:0;top:0;width:735px;height:410px;background:linear-gradient(135deg,#b9a596 0%,#d8c3b2 40%,#c8a98c 70%,#8b6a55 100%)}
.topbar{left:0;top:0;width:735px;height:42px;background:rgba(60,55,50,.55);display:flex;align-items:center;padding:0 22px;font-family:"Exo 2",sans-serif;font-size:10px;color:var(--gold)}
.topbar .nav{display:flex;gap:9px;align-items:center}
.topbar .nav.right{margin-left:auto}
.topbar .shop{border:1px solid var(--gold);padding:1px 5px;border-radius:2px}
.brand{position:absolute;left:50%;transform:translateX(-50%);font-family:"Exo 2",sans-serif;font-weight:700;font-size:19px;color:var(--white);display:flex;align-items:center;gap:8px}
.brand .dot{width:7px;height:7px;border-radius:50%;background:var(--gold)}
.side-tab{top:204px;width:14px;height:42px;background:#333;border-radius:2px;color:var(--white);font-size:6px;line-height:7px;text-align:center;padding-top:6px;font-family:"Exo 2",sans-serif}
.hero-kicker{left:254px;top:178px;font-family:"Exo 2",sans-serif;font-size:15px;letter-spacing:3px;font-weight:600;color:var(--white)}
.hero-script{left:190px;top:170px;font-family:"Great Vibes",cursive;font-size:78px;color:var(--white);white-space:nowrap}
.hero-cta{left:428px;top:257px;width:102px;height:24px;background:var(--gold);border-radius:3px;font-family:"Exo 2",sans-serif;font-weight:600;font-size:12px;letter-spacing:2px;color:var(--ink);display:flex;align-items:center;justify-content:center}

/* section titles */
.section-title{font-family:"Exo 2",sans-serif;font-weight:500;font-size:20px;color:var(--gold);display:flex;align-items:center;gap:10px;justify-content:center;width:735px;left:0}
.section-title .dot{width:6px;height:6px;border-radius:50%;background:var(--gold)}
.intro{left:200px;width:335px;top:463px;font-size:7.2px;line-height:11px;color:var(--muted);text-align:center}

/* grid */
.photo{display:block}
.tile-text{background:var(--panel);padding:36px 21px 0}
.tile-text .script{font-family:"Great Vibes",cursive;font-size:13px;color:#333}
.tile-text h3{font-family:"Exo 2",sans-serif;font-weight:500;font-size:15px;letter-spacing:.5px;margin-top:6px}
.tile-text .price{font-size:8px;color:#444}
.tile-text .price b{color:var(--gold);font-weight:600}
.btn-outline{display:inline-block;border:1px solid var(--gold);padding:2px 6px;font-family:"Exo 2",sans-serif;font-size:8px;letter-spacing:1.5px;font-weight:600;margin-top:28px;color:var(--ink);background:var(--white)}
.overlay-band{left:0;width:100%;height:66px;top:54px;background:rgba(255,255,255,.35);display:flex;flex-direction:column;align-items:center;justify-content:center}
.overlay-band .script{font-family:"Great Vibes",cursive;font-size:12px;color:#333}
.overlay-band h3{font-family:"Exo 2",sans-serif;font-weight:500;font-size:14px;letter-spacing:.5px;color:var(--ink)}

/* posts */
.arrow-btn{top:887px;width:16px;height:16px;border:1px solid var(--gold);border-radius:2px}
.view-all{left:638px;top:887px;width:65px;height:16px;border:1px solid var(--gold);border-radius:2px;font-family:"Exo 2",sans-serif;font-size:8px;letter-spacing:1.5px;font-weight:600;display:flex;align-items:center;justify-content:center}
.strip{left:0;top:922px;width:735px;height:111px;display:flex}
.strip div{flex:1}
.foot-nav{left:0;top:1049px;width:735px;text-align:center;font-family:"Exo 2",sans-serif;font-size:7px;letter-spacing:.5px;color:var(--ink)}

/* footer */
.footer{left:0;top:1072px;width:735px;height:102px;display:flex}
.footer .col{flex:1;background:var(--foot);text-align:center;padding-top:16px;color:#bbb;font-size:7px}
.footer .col.mid{background:var(--foot-mid)}
.footer h4{font-family:"Exo 2",sans-serif;font-weight:500;font-size:12px;color:var(--gold);margin-bottom:11px;letter-spacing:.5px}
.contact-line{display:flex;align-items:center;justify-content:center;gap:5px;line-height:14px}
.contact-line a{color:var(--gold);text-decoration:none}
.socials{display:flex;gap:8px;justify-content:center;margin-top:10px}
.socials span{width:24px;height:22px;border:1px solid #555}
.news-form{display:flex;margin:10px auto 0;width:183px;height:22px}
.news-form .field{flex:1;border:1px solid #555;font-size:6px;color:#999;text-align:left;padding:6px 7px}
.news-form .go{width:22px;background:var(--gold);display:flex;align-items:center;justify-content:center}
.copy{left:0;top:1182px;width:735px;text-align:center;font-size:7px;color:var(--muted)}
</style>
</head>
<body>

<div class="abs hero" role="img" aria-label="Fashion photo of a blonde woman in sparkling tights seated beside an ornate brass bed"></div>
<header class="abs topbar">
  <nav class="nav"><span>About</span>-<span>Charity</span>-<span>Locations</span>-<span>Contact</span></nav>
  <div class="brand"><span class="dot"></span>TIDE HOLLOW 7</div>
  <nav class="nav right"><span class="shop">SHOP</span>-<span>Cart(0)</span>-<span>My Account</span>-
    <svg width="9" height="9" viewBox="0 0 10 10"><circle cx="4" cy="4" r="3" fill="none" stroke="#f6b72c" stroke-width="1.5"/><line x1="6.3" y1="6.3" x2="9" y2="9" stroke="#f6b72c" stroke-width="1.5"/></svg>
  </nav>
</header>
<div class="abs side-tab" style="left:30px">P<br>R<br>E<br>V</div>
<div class="abs side-tab" style="left:690px">N<br>E<br>X<br>T</div>
<div class="abs hero-script">huge collection</div>
<div class="abs hero-kicker">NEW TREND</div>
<div class="abs hero-cta">SHOP NOW</div>
<svg class="abs" style="left:360px;top:366px" width="15" height="20" viewBox="0 0 15 20"><path d="M7.5 1v17M1 11.5l6.5 6.5 6.5-6.5" fill="none" stroke="#fff" stroke-width="2"/></svg>

<h2 class="abs section-title" style="top:434px"><span class="dot"></span>LATEST IN<span class="dot"></span></h2>
<p class="abs intro">Lorem ipsum dolor sit amet, consectetuer adipiscing elit, sed diam nonummy nibh euismod tincidunt ut laoreet dolore magna aliquam erat volutpat.</p>

<div class="abs photo" style="left:30px;top:502px;width:214px;height:175px;background:linear-gradient(135deg,#8d8f98,#c9beaa)" role="img" aria-label="Grey wrap bracelets with silver and gold medallion charms"></div>
<div class="abs tile-text" style="left:244px;top:502px;width:204px;height:175px">
  <div class="script">emphasize jewelry</div>
  <h3>NEW PRODUCTS</h3>
  <div class="price">From to <b>$30.00</b></div>
  <span class="btn-outline">SHOP NOW</span>
</div>
<div class="abs photo" style="left:448px;top:502px;width:257px;height:175px;background:linear-gradient(180deg,#dcdcdc,#8a7a72)" role="img" aria-label="Sparkling bronze cuff bracelet with a stone setting">
  <div class="abs overlay-band"><span class="script">chic jewelry</span><h3>HOMEBASE</h3></div>
</div>
<div class="abs photo" style="left:30px;top:677px;width:256px;height:174px;background:linear-gradient(135deg,#5aa8c0,#8a6a4a 60%,#c4c0b6)" role="img" aria-label="Turquoise bead necklace with silver medal pendants on wood">
  <div class="abs overlay-band"><span class="script">chic jewelry</span><h3>HOME DESIGN</h3></div>
</div>
<div class="abs photo" style="left:286px;top:677px;width:215px;height:174px;background:linear-gradient(135deg,#e8e4de,#b8a48e 55%,#3a3a4a)" role="img" aria-label="Fashion photo of a woman seated on a bed by a brass headboard"></div>
<div class="abs tile-text" style="left:501px;top:677px;width:204px;height:174px">
  <div class="script">women's fashion</div>
  <h3>NEW PRODUCTS</h3>
  <div class="price">From to <b>$20.00</b></div>
  <span class="btn-outline">SHOP NOW</span>
</div>

<svg class="abs arrow-btn" style="left:30px" viewBox="0 0 16 16"><path d="M10 4l-5 4 5 4z" fill="#555"/></svg>
<svg class="abs arrow-btn" style="left:50px" viewBox="0 0 16 16"><path d="M6 4l5 4-5 4z" fill="#555"/></svg>
<h2 class="abs section-title" style="top:882px"><span class="dot"></span>POPULAR POSTS<span class="dot"></span></h2>
<div class="abs view-all">VIEW ALL</div>
<div class="abs strip">
  <div style="background:linear-gradient(135deg,#d8b8a0,#3e8a9a)" role="img" aria-label="Beaded necklaces on art cards"></div>
  <div style="background:linear-gradient(180deg,#e6c640,#8a6a4a)" role="img" aria-label="Yellow flowers on a wooden stump"></div>
  <div style="background:linear-gradient(180deg,#c8c8c8,#6a5a55)" role="img" aria-label="Bronze cuff bracelet"></div>
  <div style="background:linear-gradient(135deg,#5a5e6a,#b8b8b8)" role="img" aria-label="Silver medallion charm on grey wrap"></div>
  <div style="background:linear-gradient(135deg,#4aa0b4,#6a4a30)" role="img" aria-label="Turquoise bead necklace with medals"></div>
  <div style="background:linear-gradient(135deg,#d8d0c0,#1e2a78)" role="img" aria-label="Navy wrap bracelet with gold charm"></div>
  <div style="background:linear-gradient(135deg,#2aa0c0,#6ac0d0)" role="img" aria-label="Turquoise wrap bracelets"></div>
</div>
<nav class="abs foot-nav">SHOP &nbsp;-&nbsp; ABOUT &nbsp;-&nbsp; CHARITY &nbsp;-&nbsp; LOCATIONS &nbsp;-&nbsp; CONTACT</nav>

<footer class="abs footer">
  <div class="col">
    <h4>CONTACT US</h4>
    <div class="contact-line"><svg width="7" height="8" viewBox="0 0 8 10"><path d="M4 0a3.5 3.5 0 0 0-3.5 3.5C.5 6 4 10 4 10s3.5-4 3.5-6.5A3.5 3.5 0 0 0 4 0z" fill="#bbb"/><circle cx="4" cy="3.5" r="1.2" fill="#2e2e2e"/></svg>Unit 12, Harbor Row, Port Elwin</div>
    <div class="contact-line"><svg width="7" height="7" viewBox="0 0 10 10"><path d="M2 0l2 2.5-1.2 1.5a6 6 0 0 0 3 3L7.5 5.8 10 8 8.5 10C4 10 0 6 0 1.5z" fill="#bbb"/></svg>(+101) 555 0142 778</div>
    <div class="contact-line"><svg width="8" height="6" viewBox="0 0 10 7"><rect x=".5" y=".5" width="9" height="6" fill="none" stroke="#bbb"/><path d="M.5.5L5 4 9.5.5" fill="none" stroke="#bbb"/></svg><a>hello@tidehollow7.com</a></div>
  </div>
  <div class="col mid">
    <h4>CONNECT WITH US</h4>
    <div>Join the conversation about Tide Hollow 7</div>
    <div class="socials"><span></span><span></span><span></span><span></span><span></span></div>
  </div>
  <div class="col">
    <h4>NEWSLETTER</h4>
    <div>Lorem ipsum dolor sit consectetuer adipiscing elit</div>
    <div class="news-form"><div class="field">Your email address...</div><div class="go"><svg width="8" height="8" viewBox="0 0 8 8"><path d="M0 4h7M4 1l3 3-3 3" fill="none" stroke="#fff"/></svg></div></div>
  </div>
</footer>
<p class="abs copy">All rights reserved. © 2016 Tide Hollow 7</p>

</body>
</html>
```